Text Box for making an update on our website

We need an awesome "Text Box" so that our Users can make an amazing Post or update on our website or App.

Let's make something super duper like Pictavo, Friendloop, Chirr or Qmeld text box but a bit more amazing....

I've included our current desktop and Mobile "Text Box" which needs love :)

Our Text Box by default makes a Post "Private" the User can change it to "Public"

I have included what a final "Post" looks like on our site.

Could we incorporate a bit of the "Post" design into the "Create Post" design..... maybe make the header similar.

thanks

Morgan

Target Market(s)

Health Care, Hospitals, Caregivers, Nurses

Industry/Entity Type

Health Care

Font styles to use
Other font styles liked:
• Comfortaa

Requirements
Must have
• Our main colors are

#1D44B8 - Blue
#D85097 - Pink
Nice to have
• Super clean and simple. Happy and Easy to use
Should not have
• Complicated

Too many colors

```html
<!DOCTYPE html>
<html lang="en">
<head>
<meta charset="utf-8">
<title>Create Post – Composer States</title>
<link rel="stylesheet" href="https://fonts.googleapis.com/css2?family=Source+Sans+3:wght@400;500&display=swap">
<style>
  :root {
    --blue: #2a51b9;
    --pink: #d65597;
    --page: #f5f5f5;
    --white: #ffffff;
    --toolbar: #dcdcdc;
    --field-border: #c8c8c8;
    --placeholder: #bdbdbd;
    --divider: #8497d2;
    --avatar-tone: #8c8a7c;
  }
  * { box-sizing: border-box; margin: 0; padding: 0; }
  html, body { width: 1200px; height: 840px; overflow: hidden; }
  body {
    background: var(--page);
    font-family: "Source Sans 3", "Myriad Pro", sans-serif;
    position: relative;
  }
  .composer {
    position: absolute;
    left: 184px;
    width: 831px;
    height: 303px;
    border-radius: 24px;
    overflow: hidden;
    background: var(--white);
    box-shadow: 6px 8px 10px rgba(0,0,0,0.22);
  }
  .composer--public { top: 61px; --accent: var(--blue); }
  .composer--private { top: 450px; --accent: var(--pink); }

  .composer__header {
    position: absolute; left: 0; top: 0; width: 100%; height: 80px;
    background: var(--accent);
    color: var(--white);
  }
  .avatar-badge {
    position: absolute; left: 19px; top: 22px; width: 24px; height: 30px;
    border: 2px solid var(--white);
    border-top: none;
    border-radius: 0 0 12px 12px;
    background: var(--pink);
  }
  .composer--private .avatar-badge { background: var(--pink); }
  .avatar {
    position: absolute; left: 33px; top: 14px; width: 46px; height: 49px;
    border-radius: 50% 50% 50% 50% / 50% 50% 50% 50%;
    border-top-right-radius: 4px;
    border: 2px solid var(--white);
    background: radial-gradient(circle at 50% 40%, #c9a98e 0%, #9c8a6e 45%, #4d5a58 100%);
  }
  .composer__name {
    position: absolute; left: 88px; top: 13px;
    font-size: 37px; font-weight: 400; letter-spacing: 0.2px; line-height: 1.2;
  }
  .lock { position: absolute; left: 555px; top: 18px; width: 27px; height: 46px; }
  .privacy-label {
    position: absolute; left: 599px; top: 28px;
    font-size: 17px; line-height: 1.2;
  }
  .toggle {
    position: absolute; left: 663px; top: 27px; width: 77px; height: 37px;
    border-radius: 19px; background: var(--white);
  }
  .toggle__knob {
    position: absolute; top: 8px; width: 21px; height: 21px; border-radius: 50%;
    background: var(--accent);
  }
  .composer--public .toggle__knob { left: 9px; }
  .composer--private .toggle__knob { right: 10px; }
  .close { position: absolute; left: 772px; top: 29px; width: 24px; height: 24px; }

  .composer__field {
    position: absolute; left: 19px; top: 99px; width: 794px; height: 81px;
    border: 2px solid var(--field-border); border-radius: 41px;
    padding-left: 26px;
    font-size: 36px; line-height: 75px; color: var(--placeholder);
  }

  .composer__toolbar {
    position: absolute; left: 0; top: 196px; width: 100%; height: 107px;
    background: var(--toolbar);
  }
  .tool {
    position: absolute; top: 18px; width: 120px; margin-left: -60px;
    text-align: center; color: var(--blue); font-size: 16.5px;
  }
  .tool svg { display: block; margin: 0 auto; width: 52px; height: 52px; }
  .tool__label { display: block; margin-top: 14px; line-height: 1; }
  .tool--photos { left: 81px; }
  .tool--checkin { left: 206px; }
  .tool--tag { left: 334px; }
  .tool--emoji { left: 431px; }
  .tool--files { left: 540px; }
  .toolbar__divider {
    position: absolute; left: 702px; top: 20px; width: 3px; height: 77px;
    background: var(--divider);
  }
  .send {
    position: absolute; left: 736px; top: 27px; width: 64px; height: 64px;
    border-radius: 50%; background: var(--blue);
  }
  .send svg { position: absolute; left: 12px; top: 14px; width: 40px; height: 36px; }
</style>
</head>
<body>

<section class="composer composer--public" aria-label="Create post, public">
  <header class="composer__header">
    <span class="avatar-badge"></span>
    <span class="avatar" role="img" aria-label="Profile photo of Nora Whitfield"></span>
    <h1 class="composer__name">Nora Whitfield</h1>
    <svg class="lock" viewBox="0 0 27 46" aria-hidden="true">
      <path d="M5 20 V11 a8.5 8.5 0 0 1 17 0 V13" fill="none" stroke="#fff" stroke-width="3.5"/>
      <rect x="0" y="20" width="27" height="26" rx="5" fill="#fff"/>
    </svg>
    <span class="privacy-label">Public</span>
    <span class="toggle"><span class="toggle__knob"></span></span>
    <svg class="close" viewBox="0 0 24 24" aria-label="Close"><path d="M2 2 L22 22 M22 2 L2 22" stroke="#fff" stroke-width="3" stroke-linecap="round"/></svg>
  </header>
  <div class="composer__field">Share a new Post, Nora!</div>
  <footer class="composer__toolbar">
    <div class="tool tool--photos">
      <svg viewBox="0 0 52 52"><path d="M9 10 h9 l3-4 h12 l3 4 h6 a6 6 0 0 1 6 6 v20 a6 6 0 0 1 -6 6 H8 a6 6 0 0 1 -6 -6 V16 a6 6 0 0 1 6 -6z" fill="#2a51b9"/><circle cx="25" cy="25" r="9" fill="none" stroke="#fff" stroke-width="3"/><circle cx="42" cy="16" r="1.5" fill="#fff"/></svg>
      <span class="tool__label">Add Photos</span>
    </div>
    <div class="tool tool--checkin">
      <svg viewBox="0 0 52 52"><path d="M26 50 C18 38 8 30 8 20 a18 18 0 0 1 36 0 c0 10 -10 18 -18 30z" fill="#d65597"/><circle cx="26" cy="20" r="10" fill="#fff"/><path d="M26 26 l-5-5 a3 3 0 0 1 5-4 a3 3 0 0 1 5 4z" fill="#d65597"/></svg>
      <span class="tool__label">Check-in</span>
    </div>
    <div class="tool tool--tag">
      <svg viewBox="0 0 52 52"><path d="M3 4 h22 l24 24 -22 22 L3 26z" fill="#2a51b9" stroke="#2a51b9" stroke-width="3" stroke-linejoin="round"/><path d="M30 39 l-8-7 a5 5 0 0 1 8-6 a5 5 0 0 1 8 6z" fill="#fff"/></svg>
      <span class="tool__label">Tag&nbsp; Friends</span>
    </div>
    <div class="tool tool--emoji">
      <svg viewBox="0 0 52 52"><circle cx="26" cy="26" r="23" fill="none" stroke="#d65597" stroke-width="3"/><path d="M17 26 l-5-4.5 a2.8 2.8 0 0 1 5-3 a2.8 2.8 0 0 1 5 3z M35 26 l-5-4.5 a2.8 2.8 0 0 1 5-3 a2.8 2.8 0 0 1 5 3z" fill="#d65597"/><path d="M19 32 a7 7 0 0 0 14 0" fill="none" stroke="#d65597" stroke-width="3" stroke-linecap="round"/></svg>
      <span class="tool__label">Emoji</span>
    </div>
    <div class="tool tool--files">
      <svg viewBox="0 0 52 52"><path d="M34 14 L14 36 a5 5 0 0 0 8 6 L44 18 a8 8 0 0 0 -12 -11 L8 33 a11 11 0 0 0 16 15 L40 30" fill="none" stroke="#2a51b9" stroke-width="3.2" stroke-linecap="round"/></svg>
      <span class="tool__label">Add Files</span>
    </div>
    <span class="toolbar__divider"></span>
    <span class="send" aria-label="Post"><svg viewBox="0 0 40 36"><path d="M2 17 L38 2 L24 34 L19 20z" fill="#fff"/><path d="M19 20 L38 2" stroke="#2a51b9" stroke-width="2.5"/></svg></span>
  </footer>
</section>

<section class="composer composer--private" aria-label="Create post, private">
  <header class="composer__header">
    <span class="avatar-badge"></span>
    <span class="avatar" role="img" aria-label="Profile photo of Nora Whitfield"></span>
    <h1 class="composer__name">Nora Whitfield</h1>
    <svg class="lock" viewBox="0 0 27 46" aria-hidden="true">
      <path d="M5 22 V11 a8.5 8.5 0 0 1 17 0 V22" fill="none" stroke="#fff" stroke-width="3.5"/>
      <rect x="0" y="20" width="27" height="26" rx="5" fill="#fff"/>
    </svg>
    <span class="privacy-label">Private</span>
    <span class="toggle"><span class="toggle__knob"></span></span>
    <svg class="close" viewBox="0 0 24 24" aria-label="Close"><path d="M2 2 L22 22 M22 2 L2 22" stroke="#fff" stroke-width="3" stroke-linecap="round"/></svg>
  </header>
  <div class="composer__field">Share a new Post, Nora!</div>
  <footer class="composer__toolbar">
    <div class="tool tool--photos">
      <svg viewBox="0 0 52 52"><path d="M9 10 h9 l3-4 h12 l3 4 h6 a6 6 0 0 1 6 6 v20 a6 6 0 0 1 -6 6 H8 a6 6 0 0 1 -6 -6 V16 a6 6 0 0 1 6 -6z" fill="#2a51b9"/><circle cx="25" cy="25" r="9" fill="none" stroke="#fff" stroke-width="3"/><circle cx="42" cy="16" r="1.5" fill="#fff"/></svg>
      <span class="tool__label">Add Photos</span>
    </div>
    <div class="tool tool--checkin">
      <svg viewBox="0 0 52 52"><path d="M26 50 C18 38 8 30 8 20 a18 18 0 0 1 36 0 c0 10 -10 18 -18 30z" fill="#d65597"/><circle cx="26" cy="20" r="10" fill="#fff"/><path d="M26 26 l-5-5 a3 3 0 0 1 5-4 a3 3 0 0 1 5 4z" fill="#d65597"/></svg>
      <span class="tool__label">Check-in</span>
    </div>
    <div class="tool tool--tag">
      <svg viewBox="0 0 52 52"><path d="M3 4 h22 l24 24 -22 22 L3 26z" fill="#2a51b9" stroke="#2a51b9" stroke-width="3" stroke-linejoin="round"/><path d="M30 39 l-8-7 a5 5 0 0 1 8-6 a5 5 0 0 1 8 6z" fill="#fff"/></svg>
      <span class="tool__label">Tag&nbsp; Friends</span>
    </div>
    <div class="tool tool--emoji">
      <svg viewBox="0 0 52 52"><circle cx="26" cy="26" r="23" fill="none" stroke="#d65597" stroke-width="3"/><path d="M17 26 l-5-4.5 a2.8 2.8 0 0 1 5-3 a2.8 2.8 0 0 1 5 3z M35 26 l-5-4.5 a2.8 2.8 0 0 1 5-3 a2.8 2.8 0 0 1 5 3z" fill="#d65597"/><path d="M19 32 a7 7 0 0 0 14 0" fill="none" stroke="#d65597" stroke-width="3" stroke-linecap="round"/></svg>
      <span class="tool__label">Emoji</span>
    </div>
    <div class="tool tool--files">
      <svg viewBox="0 0 52 52"><path d="M34 14 L14 36 a5 5 0 0 0 8 6 L44 18 a8 8 0 0 0 -12 -11 L8 33 a11 11 0 0 0 16 15 L40 30" fill="none" stroke="#2a51b9" stroke-width="3.2" stroke-linecap="round"/></svg>
      <span class="tool__label">Add Files</span>
    </div>
    <span class="toolbar__divider"></span>
    <span class="send" aria-label="Post"><svg viewBox="0 0 40 36"><path d="M2 17 L38 2 L24 34 L19 20z" fill="#fff"/><path d="M19 20 L38 2" stroke="#2a51b9" stroke-width="2.5"/></svg></span>
  </footer>
</section>

</body>
</html>
```